First of a series of workplace posters- our values statement

To produce a high quality poster of our values, we would like one in a3 and one in a4 both full colour
By utilising the supplied text , the intent is to produce a really striking poster for all our work places, which set out our company values. we are looking for really strong graphical elements which support the message visually . This will be the first of a series of posters, so we are looking to establish at stylistic theme for all with this one. for more on our business,

Target Market(s)

Internal and external audiences, our clients are all tier one companies

Requirements
Must have
• contemporary design rather than conservative, visually striking
• Must be clearly readable from a reasonable distance
Nice to have
• would be nice to tie in to the blue and greens of our logo in similar fashion to our website. www.kbtgreenworks.com
Should not have
• Difficult to read fonts,

```html
<!DOCTYPE html>
<html lang="en">
<head>
<meta charset="utf-8">
<title>Our Values – KBT Greenworks</title>
<link rel="stylesheet" href="https://fonts.googleapis.com/css2?family=Roboto+Slab:wght@400&family=Nunito+Sans:wght@600;700&display=swap">
<style>
  :root {
    --navy: #1c2b57;
    --green: #6aad00;
    --white: #ffffff;
  }
  * { margin: 0; padding: 0; box-sizing: border-box; }
  html, body { width: 829px; height: 1200px; overflow: hidden; }
  body { background: var(--green); font-family: "Nunito Sans", sans-serif; }
  .poster { position: relative; width: 829px; height: 1200px; background: var(--green); overflow: hidden; }
  .header-band { position: absolute; left: 0; top: 0; width: 829px; height: 166px; background: var(--navy); }
  .header-rule { position: absolute; left: 0; top: 166px; width: 829px; height: 4px; background: var(--white); }
  .brand-box {
    position: absolute; left: 22px; top: 0; width: 232px; height: 184px; background: var(--white);
    display: flex; align-items: center; justify-content: center; gap: 8px;
  }
  .brand-dot { width: 14px; height: 14px; border-radius: 50%; background: var(--navy); }
  .brand-name { font-family: "Nunito Sans", sans-serif; font-weight: 700; font-size: 27px; color: var(--navy); line-height: 1.1; }
  .page-title {
    position: absolute; left: 279px; top: 37px;
    font-family: "Roboto Slab", serif; font-weight: 400; font-size: 80px; line-height: 1;
    color: var(--white); letter-spacing: 1px; white-space: nowrap;
  }
  .value-item { position: absolute; left: 0; width: 829px; }
  .value-icon { position: absolute; left: 90px; width: 86px; height: 86px; }
  .value-icon svg { width: 86px; height: 86px; display: block; }
  .value-name {
    position: absolute; left: 236px;
    font-family: "Roboto Slab", serif; font-weight: 400; font-size: 46px; line-height: 1;
    color: var(--white); letter-spacing: 1px; white-space: nowrap;
  }
  .value-text {
    position: absolute; left: 236px;
    font-weight: 600; font-size: 24px; line-height: 1; color: var(--navy); white-space: nowrap;
  }
</style>
</head>
<body>
<main class="poster">
  <div class="header-band"></div>
  <div class="header-rule"></div>
  <div class="brand-box"><span class="brand-dot"></span><span class="brand-name">KBT Greenworks</span></div>
  <h1 class="page-title">OUR VALUES</h1>

  <section class="value-item" style="top:0">
    <div class="value-icon" style="top:258px">
      <svg viewBox="0 0 80 80" fill="var(--white)"><path d="M16 10h48l14 22-38 44L2 32z"/><path d="M14 60h2v-4h2v4h4v2h-4v4h-2v-4h-4zM64 50h2v-4h2v4h4v2h-4v4h-2v-4h-4z"/><path d="M4 32h72M26 10l-6 22 20 44 20-44-6-22M40 10l-14 22M40 10l14 22" stroke="var(--green)" stroke-width="2" fill="none"/></svg>
    </div>
    <h2 class="value-name" style="top:262px">VALUE</h2>
    <p class="value-text" style="top:319px">We value our people above everything else</p>
  </section>

  <section class="value-item">
    <div class="value-icon" style="top:384px">
      <svg viewBox="0 0 80 80" fill="var(--white)"><path d="M40 4C18 4 2 20 2 42h76C78 20 62 4 40 4z"/><path d="M40 0v4M40 42v30a5 5 0 0 1-10 0" stroke="var(--white)" stroke-width="2" fill="none"/><path d="M20 42C22 26 30 12 40 6M60 42C58 26 50 12 40 6M40 6v36M8 42C10 28 22 12 40 6M72 42C70 28 58 12 40 6" stroke="var(--green)" stroke-width="2" fill="none"/></svg>
    </div>
    <h2 class="value-name" style="top:391px">SAFE</h2>
    <p class="value-text" style="top:446px">All our workplaces are safe work places</p>
  </section>

  <section class="value-item">
    <div class="value-icon" style="top:524px">
      <svg viewBox="0 0 80 80" fill="var(--white)"><path d="M76 4C40 8 14 20 12 52c12 12 42 8 56-10C76 30 76 16 76 4z"/><path d="M4 78C24 56 44 40 64 22" stroke="var(--green)" stroke-width="3" fill="none"/><path d="M4 78l10-12" stroke="var(--white)" stroke-width="4" stroke-linecap="round"/></svg>
    </div>
    <h2 class="value-name" style="top:520px">BENEFITS</h2>
    <p class="value-text" style="top:579px">The planet benefits from our existence</p>
  </section>

  <section class="value-item">
    <div class="value-icon" style="top:652px">
      <svg viewBox="0 0 80 80" fill="var(--white)"><path d="M28 48l-10 28 8-4 6 6 8-26zM52 48l10 28-8-4-6 6-8-26z"/><circle cx="40" cy="32" r="30"/><circle cx="40" cy="32" r="17" fill="var(--green)"/><circle cx="40" cy="32" r="12"/></svg>
    </div>
    <h2 class="value-name" style="top:650px">PROUD</h2>
    <p class="value-text" style="top:706px">We are proud of who we are</p>
  </section>

  <section class="value-item">
    <div class="value-icon" style="top:781px">
      <svg viewBox="0 0 80 80" fill="var(--white)"><rect x="0" y="36" width="26" height="38"/><rect x="5" y="41" width="8" height="2" fill="var(--green)"/><circle cx="20" cy="62" r="3" fill="none" stroke="var(--green)" stroke-width="2"/><path d="M30 38L44 14V2c6 0 10 4 10 10v16h20c5 0 6 8 2 10 4 2 3 8-1 10 4 2 3 8-2 10 2 2 1 8-4 8H30z"/></svg>
    </div>
    <h2 class="value-name" style="top:783px">STANDARD</h2>
    <p class="value-text" style="top:841px">We set the standard</p>
  </section>

  <section class="value-item">
    <div class="value-icon" style="top:930px">
      <svg viewBox="0 0 80 80" fill="var(--white)"><path d="M10 4h60c4 10-2 24-12 28-4 8-10 12-14 12v12h10v8H26v-8h10V44c-4 0-10-4-14-12C12 28 6 14 10 4z"/><circle cx="40" cy="20" r="10" fill="none" stroke="var(--green)" stroke-width="2"/><path d="M38 16l3-2v12" stroke="var(--green)" stroke-width="2" fill="none"/><rect x="6" y="70" width="68" height="7"/><rect x="14" y="66" width="52" height="4"/></svg>
    </div>
    <h2 class="value-name" style="top:937px">SUCCEED</h2>
    <p class="value-text" style="top:991px">We succeed together</p>
  </section>
</main>
</body>
</html>
```